Lorvik.no is a new website about pedagogical entrepreneurship. It's main target group is teachers. The Fjellmark Bureau for Digital Schooling and the Halvstad Agency for Classroom Affairs are leading the project.

The web page is meant to show examples of how different methods of entrepreneurship can be used pedagogical in a learning environment. The page will also support the user with examples of different teaching programs and other examples of best practice.

Pedagogical entrepreneurship is not about business and men in suits. It's a method for learning. The focus in the design should be on school, education and new ways of learning.

The final product should be motivating and engaging, but at the same time governmental and serious. We are not looking for something "flashy" and corporate-looking, but a moderate, task-focused and clean design that state quality.

We need designs for three pages:
1 - frontpage
2 - subpage ("Metoder og undervisningsopplegg")
3 - subpage ("Tavle-KOMP i Brekkvoll")

The interaction design for these three pages will be uploaded as an attachment.

We would like you to find inspiration in the following websites:
- www.skaperlund.no
- www.guldrim.no
- www.brambelquest.com
- www.tuv.no
(more will be added)

Please use the attached logo, and feel free to use this as an inspiration for the rest of the design.

Reason: We are awaiting improved designs from some designers, and need to extend the deadline a couple of days.

Target Market(s)

Teachers

Industry/Entity Type

Education

Requirements
Must have
• * Header with: Logo. Main navigation. Utility navigation. Search box.
* Footer
Should not have
• Images of men in suits.
Very strong graphical elements that stands out too much (we want it clean).

```html
<!DOCTYPE html>
<html lang="en">
<head>
<meta charset="utf-8">
<title>Lorvik.no – Pedagogical Entrepreneurship</title>
<link href="https://fonts.googleapis.com/css2?family=Questrial&family=Arimo:wght@400;700&display=swap" rel="stylesheet">
<style>
:root{
  --blue:#1a8ad0;
  --blue-dark:#1473b4;
  --blue-light:#3fa8e6;
  --navy:#1c3a6b;
  --ink:#333;
  --muted:#666;
  --line:#d6d6d6;
  --panel:#f1f1f1;
  --white:#fff;
}
*{box-sizing:border-box;margin:0;padding:0}
html,body{width:926px;height:1200px;overflow:hidden;background:var(--white)}
body{position:relative;font-family:"Arimo",Arial,sans-serif;color:var(--ink)}
a{color:inherit}
.abs{position:absolute}
.display{font-family:"Questrial","Century Gothic",sans-serif}

/* header */
.brand{left:84px;top:14px;display:flex;align-items:center;gap:10px}
.brand-dot{width:44px;height:44px;border-radius:50%;background:var(--blue)}
.brand-name{font-family:"Questrial",sans-serif;font-size:46px;line-height:1;color:var(--blue);font-weight:400}
.brand-tag{left:166px;top:58px;font-size:9px;color:var(--navy)}
.call{right:84px;top:26px;text-align:right;font-family:"Questrial",sans-serif}
.call-label{font-size:12px;color:var(--blue)}
.call-number{font-size:19px;color:#3a3a3a;line-height:1.1}

.frame{left:86px;top:81px;width:755px;height:1083px;border:1px solid var(--line);border-radius:8px}

.utility{right:197px;top:93px;display:flex;gap:26px;font-size:9.5px;color:#888}
.social{left:731px;top:89px;display:flex;gap:3px}
.social span{width:21px;height:21px;border-radius:3px;background:var(--blue-light)}
.social span:first-child{background:#c9322b}

.mainnav{left:101px;top:117px;width:725px;height:38px;border:1px solid var(--line);border-radius:6px;background:linear-gradient(#fafafa,#ececec);display:flex;align-items:center;overflow:hidden}
.mainnav a{height:100%;width:175px;display:flex;align-items:center;justify-content:center;text-decoration:none;font-family:"Questrial",sans-serif;font-size:12.5px;color:#333;border-right:1px solid var(--line)}
.mainnav a.active{background:linear-gradient(var(--blue-light),var(--blue));color:var(--white)}
.search{margin-left:16px;display:flex;height:24px}
.search span{width:143px;border:1px solid var(--line);border-right:0;background:var(--white);font-size:8px;color:#aaa;font-style:italic;padding:7px 9px;border-radius:3px 0 0 3px}
.search b{width:28px;background:var(--blue);border-radius:0 3px 3px 0;display:flex;align-items:center;justify-content:center}

.hero{left:101px;top:165px;width:725px;height:288px;border-radius:6px;border:1px solid var(--line);background:linear-gradient(100deg,#c9cfd3 0%,#b8c0c5 45%,#9aa7b0 70%,#8e99a1 100%)}

/* feature cards */
.card{top:466px;width:229px;height:67px;border-radius:6px;background:linear-gradient(var(--blue-light),var(--blue-dark));box-shadow:0 2px 4px rgba(0,0,0,.25);color:var(--white);display:flex;align-items:center;padding-left:12px;gap:12px}
.card-icon{width:50px;height:38px;border-radius:4px;background:rgba(255,255,255,.55)}
.card-title{font-family:"Questrial",sans-serif;font-size:16px;line-height:16px}
.card-sub{font-size:8.5px;font-style:italic;margin-top:2px}

/* meter box */
.meter{left:101px;top:550px;width:229px;height:254px;border:1px solid var(--line);border-radius:5px;background:linear-gradient(#f7f7f7,#ececec);box-shadow:0 2px 3px rgba(0,0,0,.15);overflow:hidden}
.meter-head{height:42px;padding:4px 10px;font-family:"Questrial",sans-serif;font-size:14px;line-height:16px;border-bottom:1px solid var(--line);background:linear-gradient(#fafafa,#e9e9e9)}
.meter-art{margin:18px auto 0;width:200px;height:150px;border-radius:6px;background:radial-gradient(circle at 60% 50%,#e9e9e9,#dcdcdc 60%,#cfd8cf)}
.meter-link{display:block;text-align:center;margin-top:16px;font-family:"Questrial",sans-serif;font-size:13px;color:var(--blue)}

/* welcome */
.welcome{left:347px;top:562px;width:478px}
.h-blue{font-family:"Questrial",sans-serif;color:var(--blue);font-size:15.5px;font-weight:400}
.welcome p{font-size:8.5px;line-height:11.5px;color:#444;margin-top:6px}
.started{left:347px;top:666px;width:478px}
.cols{position:relative;height:130px}
.col{position:absolute;top:20px}
.col h3{font-family:"Questrial",sans-serif;font-weight:400;font-size:12px;color:#333;margin-bottom:4px}
.col li{list-style:none;font-size:8.5px;line-height:14.5px;text-decoration:underline;color:#444}
.btn{display:inline-block;margin-top:10px;font-size:8.5px;padding:2px 5px;border:1px solid #ccc;border-radius:3px;background:linear-gradient(#fff,#e8e8e8);color:#444}

/* inspiration */
.insp-bar{left:101px;top:820px;width:725px;height:35px;border:1px solid var(--line);border-radius:4px;background:linear-gradient(#fafafa,#eaeaea);font-family:"Questrial",sans-serif;font-size:18px;padding:6px 13px}
.arrow{top:902px;width:40px;height:40px}
.school{top:868px;width:207px}
.school-photo{height:107px;border-radius:3px}
.school p{font-family:"Questrial",sans-serif;font-size:13px;text-align:center;margin-top:12px;color:#333}
.divider{left:101px;top:1016px;width:725px;height:1px;background:var(--line)}

/* footer */
.foot-brand{left:101px;top:1074px;display:flex;align-items:center;gap:6px}
.foot-brand i{width:16px;height:16px;border-radius:50%;background:var(--blue)}
.foot-brand span{font-family:"Questrial",sans-serif;font-size:22px;color:var(--blue)}
.fcol{top:1036px}
.fcol h4{font-family:"Questrial",sans-serif;font-weight:400;color:var(--blue);font-size:15px;line-height:14px;margin-bottom:6px}
.fcol li{font-size:8.5px;line-height:14.5px;color:#444;list-style:none;padding-left:9px;position:relative}
.fcol li::before{content:"";position:absolute;left:0;top:6px;width:3px;height:3px;border-radius:50%;background:#444}
.fcol li span{text-decoration:underline}
.fcol li.more::before{display:none}
.fcol li.dot.more::before{display:block}
.fcol li.more span{font-size:9px;color:#333}
.bottom{top:1176px;font-size:7.5px;color:#444}
</style>
</head>
<body>

<header>
  <div class="abs brand"><span class="brand-dot"></span><span class="brand-name">Lorvik</span></div>
  <div class="abs brand-tag">Entreprenørielle metoder i undervisningen</div>
  <div class="abs call">
    <div class="call-label">Call Now to Find Out More:</div>
    <div class="call-number">555 - 018 - 274 -19</div>
  </div>
</header>

<div class="abs frame"></div>

<nav class="abs utility"><a>New User?</a><a>Register</a><a>Sign in</a><a>Help</a></nav>
<div class="abs social" aria-label="Social links"><span></span><span></span><span></span><span></span></div>

<nav class="abs mainnav">
  <a class="active">Best Practice schools</a>
  <a>Lorvikometer</a>
  <a>About Lorvik.no</a>
  <div class="search">
    <span>Search...</span>
    <b><svg width="12" height="12" viewBox="0 0 12 12"><circle cx="5" cy="5" r="3.6" fill="none" stroke="#fff" stroke-width="1.6"/><line x1="7.6" y1="7.6" x2="11" y2="11" stroke="#fff" stroke-width="1.8"/></svg></b>
  </div>
</nav>

<div class="abs hero" role="img" aria-label="Teacher at a chalkboard with chemistry formulas, pupils raising hands"></div>

<section>
  <div class="abs card" style="left:101px"><span class="card-icon" role="img" aria-label="Open book"></span><div><div class="card-title">What is Pedagocial<br>Entrepreneurship</div><div class="card-sub">Learn About what, why and how !</div></div></div>
  <div class="abs card" style="left:349px"><span class="card-icon" role="img" aria-label="Calendar"></span><div><div class="card-title">Methods and<br>Teaching Plans</div><div class="card-sub">Plan Your Lessons !</div></div></div>
  <div class="abs card" style="left:597px"><span class="card-icon" style="width:30px" role="img" aria-label="Light bulb"></span><div><div class="card-title">Good Examples /<br>Best Practice</div><div class="card-sub">Be Inspired !</div></div></div>
</section>

<aside class="abs meter">
  <div class="meter-head">Are you working<br>entrepreneurship - like</div>
  <div class="meter-art" role="img" aria-label="Gauge dial from red to green with a needle"></div>
  <a class="meter-link">Try the Lorvikometer !</a>
</aside>

<section class="abs welcome">
  <h2 class="h-blue">Welcome to Pedagogical Entrepreneurship</h2>
  <p>Lorem Ipsum is simply dummy text of the printing and typesetting industry. Lorem Ipsum has been the industry's standard dummy text ever since the 1500s, when an unknown printer took a galley of type and scrambled it to make a type specimen book.</p>
  <p style="margin-top:11px">It has survived not only five centuries, but also the leap into electronic typesetting, remaining essentially unchanged. It was popularised in the 1960s with the release of Letraset sheets containing Lorem Ipsum passages.</p>
</section>

<section class="abs started">
  <h2 class="h-blue">Get Started</h2>
  <div class="cols">
    <div class="col" style="left:0"><h3>Methods</h3><ul><li>Lorem Ipsum</li><li>typesetting industry</li><li>Scrambled</li><li>Electronic typesetting</li><li>Letraset sheets</li></ul><span class="btn">See More</span></div>
    <div class="col" style="left:183px"><h3>Teaching Plans</h3><ul><li>Lorem Ipsum</li><li>typesetting industry</li><li>Scrambled</li><li>Electronic typesetting</li><li>Letraset sheets</li></ul><span class="btn">See More</span></div>
    <div class="col" style="left:385px"><h3>Services</h3><ul><li>Lorem Ipsum</li><li>typesetting industry</li><li>Scrambled</li><li>Electronic typesetting</li><li>Letraset sheets</li></ul><span class="btn">See More</span></div>
  </div>
</section>

<section>
  <h2 class="abs insp-bar" style="font-weight:400">Inspiration</h2>
  <svg class="abs arrow" style="left:100px" viewBox="0 0 40 40"><circle cx="20" cy="20" r="18.5" fill="#e8e8e8" stroke="#b5b5b5" stroke-width="1.5"/><polygon points="25,11 13,20 25,29" fill="#fff" stroke="#aaa"/></svg>
  <svg class="abs arrow" style="left:787px" viewBox="0 0 40 40"><circle cx="20" cy="20" r="18.5" fill="#e8e8e8" stroke="#b5b5b5" stroke-width="1.5"/><polygon points="15,11 27,20 15,29" fill="#fff" stroke="#aaa"/></svg>
  <figure class="abs school" style="left:146px"><div class="school-photo" role="img" aria-label="Brick school building with columns" style="background:linear-gradient(#8fa7c4,#a0644a 45%,#7b5a48)"></div><p>Tavle-KOMP at Brekkvoll School</p></figure>
  <figure class="abs school" style="left:360px"><div class="school-photo" role="img" aria-label="Brick school building with lawn" style="background:linear-gradient(#5a8fd6,#9a6a52 40%,#8f6a55 70%,#6f8f4e)"></div><p>Tavle-KOMP at Brekkvoll School</p></figure>
  <figure class="abs school" style="left:573px"><div class="school-photo" role="img" aria-label="White school building with plaza" style="background:linear-gradient(#c7d9ea,#5f7f4a 35%,#e6e2da 55%,#7a9a5a)"></div><p>Tavle-KOMP at Brekkvoll School</p></figure>
</section>

<div class="abs divider"></div>

<footer>
  <div class="abs foot-brand"><i></i><span>Lorvik</span></div>
  <div class="abs fcol" style="left:197px"><h4>Pedagogical<br>Entrepreneurship</h4><ul><li style="line-height:11px"><span>What is pedagogical<br>entrepreneurship</span></li><li><span>Science</span></li><li><span>Best Practice Schools</span></li><li><span>Lorvikometeret</span></li><li><span>About Lorvik.no</span></li></ul></div>
  <div class="abs fcol" style="left:384px;top:1042px"><h4 style="margin-bottom:12px">Methods</h4><ul><li><span>Story line</span></li><li><span>Real</span></li><li><span>Cafe Pedagogical</span></li><li class="more"><span>See More</span></li></ul></div>
  <div class="abs fcol" style="left:538px;top:1042px"><h4 style="margin-bottom:12px">Gode eksempler</h4><ul><li><span>Lorem Ipsum</span></li><li><span>typesetting industry</span></li><li><span>Scrambled</span></li><li><span>Electronic typesetting</span></li><li class="dot more"><span>See More</span></li></ul></div>
  <div class="abs fcol" style="left:717px;top:1042px"><h4 style="margin-bottom:12px">Teaching Plans</h4><ul><li><span>Lorem Ipsum</span></li><li><span>typesetting industry</span></li><li><span>Scrambled</span></li><li><span>Electronic typesetting</span></li><li class="dot more"><span>See More</span></li></ul></div>

  <div class="abs bottom" style="left:99px">Best Practice schools &nbsp;|&nbsp; Lorvikometer &nbsp;|&nbsp; About Lorvik.no</div>
  <div class="abs bottom" style="right:98px">© Copyrights 2012 All rights Reserved</div>
</footer>

</body>
</html>
```